Voravolt Sports Performance Poster

We are in need of a poster for our upcoming summer Sports Performance Program during June and July.
This program caters to youth and teen athletes playing volleyball, soccer, and basketball.
Please see attached word document with program details for the poster.

MUST HAVES:
- Size needed 11x17 with bleeding for printing
- .PSD File Format WITH LAYERS (CS3 Compatible - Fonts included)*** A MUST
- Use Voravolt Bootcamps Logo
- Use Information in the attached word doc

Requirements
Must have
• - Size needed 11x17 with bleeding for printing
• - .PSD File Format WITH LAYERS (CS3 Compatible - Fonts included)*** A MUST
• - Use Voravolt Bootcamps Logo
• - Use Information in the attached word doc

```html
<!DOCTYPE html>
<html lang="en">
<head>
<meta charset="utf-8">
<title>Voravolt Sports Performance Poster</title>
<link href="https://fonts.googleapis.com/css2?family=Oswald:wght@500&family=Lato:wght@400;700&display=swap" rel="stylesheet">
<style>
  :root {
    --page-bg: #ececec;
    --concrete-light: #d3cfcb;
    --concrete-mid: #c3beb9;
    --concrete-dark: #aaa5a0;
    --ink: #161616;
    --white: #ffffff;
    --rust: #a9692b;
    --navy-blue: #2e62a2;
    --rule: rgba(255,255,255,0.75);
  }
  * { margin: 0; padding: 0; box-sizing: border-box; }
  html, body { width: 1200px; height: 1000px; overflow: hidden; background: var(--page-bg); }
  .poster {
    position: absolute; left: 338px; top: 68px; width: 558px; height: 860px;
    background:
      radial-gradient(circle at 30% 20%, var(--concrete-light), transparent 60%),
      radial-gradient(circle at 80% 75%, var(--concrete-dark), transparent 55%),
      var(--concrete-mid);
    font-family: "Lato", sans-serif;
  }
  .logo-plate {
    position: absolute; left: 40px; top: 35px; width: 477px; height: 157px;
    background: var(--white); border: 5px solid var(--ink); border-radius: 12px;
    display: flex; flex-direction: column; align-items: center; justify-content: center;
    font-family: "Oswald", sans-serif; font-weight: 500; color: var(--ink);
    text-transform: uppercase; text-align: center;
  }
  .logo-name { font-size: 44px; line-height: 46px; letter-spacing: 2px; }
  .logo-tagline { margin-top: 10px; font-size: 16px; line-height: 18px; letter-spacing: 4px; }
  .hero-art {
    position: absolute; left: 0; top: 205px; width: 558px; height: 350px;
  }
  .program-banner {
    position: absolute; left: 40px; top: 564px; width: 477px; height: 84px;
    background: var(--rust); border-radius: 12px 12px 0 0;
    color: var(--white); font-family: "Oswald", sans-serif; font-weight: 500;
    font-size: 24px; line-height: 31px; text-align: center; padding-top: 12px;
    text-transform: uppercase; white-space: nowrap;
  }
  .details-panel {
    position: absolute; left: 40px; top: 646px; width: 477px; height: 191px;
    background: var(--navy-blue); border-radius: 12px; color: var(--white);
    padding: 0 16px;
  }
  .details-row { display: flex; justify-content: space-between; align-items: center; }
  .audience { height: 44px; font-size: 15px; border-bottom: 1px solid var(--rule); }
  .dates {
    height: 46px; justify-content: center; gap: 28px; font-weight: 700; font-size: 19px;
    border-bottom: 1px solid var(--rule);
  }
  .schedule { padding-top: 8px; align-items: flex-start; }
  .times { font-size: 12.5px; line-height: 20px; font-weight: 700; }
  .pricing { text-align: right; font-size: 19px; line-height: 26px; }
  .pricing strong { font-size: 20px; }
  .pricing-rule { border-top: 1px solid var(--rule); margin: 4px 0 0 90px; }
  .capacity { font-size: 12.5px; font-weight: 700; margin-top: 6px; }
</style>
</head>
<body>
  <main class="poster">
    <header class="logo-plate">
      <div class="logo-name">Voravolt<br>Bootcamps</div>
      <div class="logo-tagline">The Ultimate Fitness Solution</div>
    </header>

    <svg class="hero-art" role="img" aria-label="Watercolour silhouettes of four young athletes jumping in the air" viewBox="0 0 558 350">
      <defs>
        <linearGradient id="rainbow" x1="0" y1="0" x2="1" y2="0">
          <stop offset="0" stop-color="#e9d233"/>
          <stop offset="0.2" stop-color="#4cb84a"/>
          <stop offset="0.38" stop-color="#e9542a"/>
          <stop offset="0.6" stop-color="#c93a9e"/>
          <stop offset="0.8" stop-color="#2d9aa8"/>
          <stop offset="1" stop-color="#2f5fb5"/>
        </linearGradient>
        <radialGradient id="fade" cx="0.5" cy="0.5" r="0.6">
          <stop offset="0" stop-color="#fff" stop-opacity="1"/>
          <stop offset="1" stop-color="#fff" stop-opacity="0"/>
        </radialGradient>
        <mask id="soft"><rect width="558" height="350" fill="url(#fade)"/></mask>
      </defs>
      <rect x="20" y="10" width="520" height="330" rx="60" fill="url(#rainbow)" opacity="0.75" mask="url(#soft)"/>
    </svg>

    <section class="program-banner">
      Voravolt’s Sports Performance Program<br>
      Speed — Agility — Power
    </section>

    <section class="details-panel">
      <div class="details-row audience"><span>Youth and Teen Programs</span><span>Ages 8-17</span></div>
      <div class="details-row dates"><span>June 5th – 30th</span><span>|</span><span>July 5th – 31st</span></div>
      <div class="details-row schedule">
        <div class="times">
          Monday, Wednesday, Friday<br>
          Youth – 9:30-10:30am<br>
          Teen – 10:30-11:30am<br>
          Teen – 3:30-4:30pm
        </div>
        <div class="pricing">
          <strong>$119</strong> per month or<br>
          <strong>$199</strong> for both months
          <div class="pricing-rule"></div>
          <div class="capacity">Limited Space – 15 spots per time track</div>
        </div>
      </div>
    </section>
  </main>
</body>
</html>
```